Storm Restoration Contractor needs a professional business card design

Looking for a professional business card design. Not looking for your cheapo MS Word standard ones that are readily available. Dont want it to be cookie cutter look like ones readily available online. We just recently changed our logo and want to freshen up all our documents. Our company handles restoring a property back to a pre-loss condition after a storm damages it. For example, wind, hail, flood, fire losses.

Target Market(s)

Property Owners, Homeowners, Property Owners, Commercial Property Owners, Property Management Companies, Hail and Wind Damaged Properties

Industry/Entity Type

Construction Company

Contact Information for Business Card

Brightline Facades
847-555-0193
847-555-0147 fax
www.brightlinefacades.example
info@brightlinefacades.example

Requirements
Must have
• Clean, Professional, fresh look
• Storm Restoration, Roofing, Siding, Windows
Nice to have
• If there is a way to incorporate storms that may be cool.

```html
<!DOCTYPE html>
<html lang="en">
<head>
<meta charset="utf-8">
<title>Brightline Facades – Business Card</title>
<link rel="stylesheet" href="https://fonts.googleapis.com/css2?family=Montserrat:wght@400;500;700;800&display=swap">
<style>
  :root {
    --brand-blue: #1b78c2;
    --ink-gray: #4a4a4c;
    --soft-gray: #6d6e71;
    --paper: #ffffff;
    --backdrop: #2b2c2e;
  }
  * { box-sizing: border-box; margin: 0; padding: 0; }
  html, body { width: 1200px; height: 900px; overflow: hidden; }
  body {
    background: var(--backdrop);
    font-family: "Montserrat", Arial, sans-serif;
    position: relative;
  }
  .card {
    position: absolute;
    width: 630px;
    height: 360px;
    border-radius: 26px;
    overflow: hidden;
  }
  /* Back side */
  .card-back {
    left: 110px; top: 60px;
    background: var(--brand-blue);
    color: var(--paper);
    text-align: center;
  }
  .card-back .brand-ring { position: absolute; left: 253px; top: 58px; }
  .card-back .brand-name {
    position: absolute; left: 0; right: 0; top: 212px;
    font-size: 32px; font-weight: 800; letter-spacing: 2px;
    text-transform: uppercase;
  }
  .card-back .web {
    position: absolute; left: 0; right: 0; top: 292px;
    font-size: 16px; font-weight: 500; letter-spacing: .3px;
  }
  /* Front side */
  .card-front {
    left: 460px; top: 480px;
    background: var(--paper);
  }
  .card-front .band { position: absolute; inset: 0; }
  .card-front .brand-name {
    position: absolute; left: 40px; top: 34px;
    color: var(--brand-blue);
    font-size: 44px; font-weight: 800; line-height: 44px;
    text-transform: uppercase; letter-spacing: 1px;
  }
  .card-front .person { position: absolute; left: 40px; top: 150px; }
  .person .name { color: var(--brand-blue); font-size: 25px; font-weight: 700; }
  .person .role { color: var(--soft-gray); font-size: 14px; font-weight: 500; margin-top: 2px; }
  .card-front .services {
    position: absolute; left: 175px; top: 220px;
    transform-origin: left bottom;
    transform: rotate(-7.2deg);
    color: var(--ink-gray);
    font-size: 15px; font-weight: 500; white-space: nowrap;
  }
  .services .dot { color: var(--brand-blue); margin: 0 5px; }
  .card-front .contacts {
    position: absolute; left: 38px; top: 276px;
    list-style: none; color: var(--paper);
    font-size: 14.5px; line-height: 20px;
  }
  .contacts li { display: flex; align-items: center; gap: 9px; }
  .contacts svg { width: 12px; height: 12px; flex: none; }
  .contacts strong { font-weight: 700; }
</style>
</head>
<body>

<section class="card card-back">
  <svg class="brand-ring" width="124" height="124" viewBox="0 0 124 124" aria-hidden="true">
    <circle cx="62" cy="62" r="56" fill="none" stroke="#ffffff" stroke-width="9"/>
  </svg>
  <div class="brand-name">Brightline Facades</div>
  <div class="web">www.brightlinefacades.example</div>
</section>

<section class="card card-front">
  <svg class="band" width="630" height="360" viewBox="0 0 630 360" aria-hidden="true">
    <polygon points="0,268 630,188 630,360 0,360" fill="#1b78c2"/>
    <polygon points="0,248 20,262 0,276" fill="#4a4a4c"/>
    <circle cx="566" cy="132" r="52" fill="#ffffff" stroke="#1b78c2" stroke-width="8"/>
  </svg>

  <div class="brand-name">Brightline<br>Facades</div>

  <div class="person">
    <div class="name">Devon Harper</div>
    <div class="role">Director</div>
  </div>

  <div class="services">
    Storm Restoration<span class="dot">•</span>Roofing<span class="dot">•</span>Siding<span class="dot">•</span>Windows
  </div>

  <ul class="contacts">
    <li>
      <svg viewBox="0 0 12 12" aria-hidden="true"><path d="M2.5 1 L4.5 1 L5.2 3.6 L4 4.6 Q5 7 7.4 8 L8.4 6.8 L11 7.5 L11 9.5 Q10.5 11 9 11 Q1 10 1 3 Q1 1.5 2.5 1Z" fill="#fff"/></svg>
      847-555-0193
    </li>
    <li>
      <svg viewBox="0 0 12 12" aria-hidden="true"><rect x="3" y="1" width="6" height="3.5" fill="#fff"/><rect x="1" y="5" width="10" height="4.5" rx="1" fill="#fff"/><rect x="3" y="8" width="6" height="3" fill="#fff"/></svg>
      847-555-0147
    </li>
    <li>
      <svg viewBox="0 0 12 12" aria-hidden="true"><rect x="1" y="2.5" width="10" height="7" fill="none" stroke="#fff" stroke-width="1.3"/><path d="M1 3 L6 7 L11 3" fill="none" stroke="#fff" stroke-width="1.3"/></svg>
      info@brightlinefacades.example
    </li>
    <li>
      <svg viewBox="0 0 12 12" aria-hidden="true"><circle cx="6" cy="6" r="5" fill="#fff"/><path d="M1 6 H11 M6 1 Q3 6 6 11 M6 1 Q9 6 6 11" fill="none" stroke="#1b78c2" stroke-width=".9"/></svg>
      www.<strong>brightlinefacades</strong>.example
    </li>
  </ul>
</section>

</body>
</html>
```